webpage design for www.brightpathYOU.com

Hi-
I am creating a website about weight loss through healthy eating. The target audience is 80% women, of all races and ethnic backgrounds, in the 35-55 age range, all of whom are overweight and want to lose weight.
At first (which is where you come in), the website will be strictly informational, and products for sale will be added later.
Obviously not all of the following information can be incorporated into the design, but to give you some background, here is what I am doing.
First thing the site visitor needs to know is what the website is about. It’s about them, and how they can lose weight effectively. It’s only secondarily about me, and the w
ebsite must talk about me only from the point of view of how can I help them. It is your job to create a webpage where I can do just that. I have the content of this page ready to go, but I need you to create a beautiful, enticing, and effective framework to put it all in. You do not need to enter any copy except for the small amount noted below.
My clients are looking for a weight loss method or program that is effective, healthy, and long-lasting. This system addresses those needs. It's important for the clients to know that with the brightpathYOU system, there is no hunger, no deprivation, no pills, no weighing foods or calorie counting, no special products to buy, among other things.
And not only does the weight come off, but there are other health benefits as well. The brightpathYOU system can lower cholesterol, blood pressure, dependence on insulin for type 2 diabetics, reduce risk of heart disease and certain types of cancer, among other things-and this has been medically documented.
When I say "healthy eating", the focus of this program is on vegetables, fruits, and grains, with no added fat, but I do not want the main page to highlight that, since the whole notion of lots of veggies can scare people away. Pictures of fruits and veggies are fine. I'll introduce scary words like “vegan” and “no added fat” into the written materials and in the video, but there is no point in chasing people away too quickly!
The banner headline should have incorporated into it, in addition to the business name, the following: "Lose weight...improve your looks...improve your health...transform your life". You will need to choose a typeface and add this copy.
I would like to have a collage of healthy, happy, slender people of all ages (mostly women), in group and social settings-but not all exercising or doing yoga or jogging, since many of my target audience are couch potatoes (at least right now). If you do use any pictures of overweight people, they should be solitary, not part of a group, and definitely not looking happy!. I was thinking of having this only in the banner at top, but if you find a way to make the site attractive by adding a thin border with this as well, feel free.
Or, since I am not a design person by any stretch of the imagination, if you have another idea as to the banner design and the rest, I am certainly open to it.
In addition to the banner headline, I want a two-column design on the lower section, one being a narrower sidebar on the right, with a place for the customer to enter his/her name, and the following: Free video & eBook" "Every Plate Tells A Story, Every Meal Builds A Habit-And How You Can Shape Yours Today", and they get this in exchange for entering their first and last name, and email address. I can link this to AWeber later. I have a video widget, as well as a bunch more, in place, so you do not need to create or order those.
I will later add something to this section about no spam will be sent.
Below that in the same thinner column on the right should be an archives section, which you will need to create if the Wordpress theme doesn't have it already. This should be the same on all pages, except the single column pages, and since they will have sales pitches, should not have anything else.
The wider, main column I want to have three particular areas: One, is video. Two is text. Three is comments.
I will be using a LOT of video, but below each video I want to be able to place the text for the video (not everyone wants to watch a video), I want a static first page, but no comments section on the first page (I may want to add a comments section later, but not now).
The next page will be a basic "about me" page. This will be a video with text below in the main section, and will have the same enter your email info on the right side bar. No need to have "comments" below this. I've uploaded a picture of me, which should appear on this page, as well as on the main page.
Then will be a blog page, again the same layout: videos, which I can add to consecutively, with "comments" below, (which I can approve or disapprove before they get posted), with the offer in the right sidebar. Any videos will also show up in the archives section.
And a "recipes" page, video and text, plus comments section, with the email offer in the sidebar. These will show up as an archives section as well. I’ll add recipes and cooking videos later.
Then will be a "Products" page, which will for now be blank (I haven't created them yet), but with the email offer in the right side bar. No comments section to this one.
And a Contact Us page, no comments section either. I'll add the contact information later.
Across bottom of each page, perhaps in a somewhat contrasting color, will be a disclaimer, which I’ll need to be able to edit. This will be in small print, and should say something like, “This website expresses the opinions of the author, is intended for informational and educational purposes only, should not be construed as medical or dietary advice, and is not intended to be a substitute for same. Before changing diets, medications, or before undertaking a weight loss regimen, be sure to consult with your physician. This information is not intended to diagnose or treat any illness or health problems you may be experiencing, so kindly address your doctor with these concerns.” You can copy and paste this text.
Each page should also say “copyright 2014, Ned Brook”, which you will need to add.
Beyond that I will need single blank column pages which I will later make into landing, thank you, and so on pages. This will not be visible from the main page, though.

This will be done in Wordpress. I have the URL and the page is set up on Wordpress already, but I will need you to integrate the design into my Wordpress site when it is completed, so you will need a working knowledge of Wordpress. So the final winner will need to have the capability of coding the design and uploading it into my website and server. When you are done, it will be a complete and turnkey website, and all I have to do is add the copy and videos.

I am not particular as to a Wordpress theme, as long as it's an unpaid one, but if you find a paid one that you think is useable and needs to be paid for, let me know so I can check it out.
And I will need to be easily able to change and edit anything in the webpage on Wordpress at the end, after you are finished, with NO HTML, so any theme must be dummy friendly (I am the dummy, by the way!). (I have a basic familiarity with Wordpress, but none of HTML.)

Hopefully this gives you more than enough information to work with. Even though this page is a bit complicated, the actual website should be pretty simple looking, not busy or full of distractions, with only a few focal points.
Updates

Hi-information has been updated, I've changed my status to "committed", and I've uploaded a lot of pictures of fruit and veggies for you to use.  Thanks for your attention!
Ned

Target Market(s)

As stated above, "The target audience is 80% women, of all races and ethnic backgrounds, in the 35-55 age range, all of whom are overweight and want to lose weight."

Industry/Entity Type

Cooking

Font styles to use
Serif

Requirements
Must have
• The home page serves two purposes: one, to introduce the reader to the material, but two, and equally important, to build my email list. To that end, the opt in form on the right should say prominently, Free video & eBook" "Every Plate Tells A Story, Every Meal Builds A Habit-And How You Can Shape Yours Today", and below that should be the opt in boxes.
The banner can be scrolling, to attract ATTENTION, should lead to the ACTION of watching the video, which will have in it a CALL TO ACTION of signing up for the hopefully compelling OFFER of the free ebook and video-and of course the newsletter. My purpose on page one is to directly address the question of "What's in it for me?", and then to deliver with the video and ebook offer.
I've uploaded a bunch of pictures of veggies and fruit-feel free to use them, as they are all mine.
Possibly a scrolling banner could be used with alternating pictures of happy, slender people alternating with pictures, and the captions of "lLose weight...improve your looks...improve your health...transform your life"

Emphasis should be on healthy eating, not on pounds lost or measuring one's waist or some such thing.

Banner headline should include: ""Lose weight...improve your looks...improve your health...transform your life"
Should not have
• Please avoid pictures of picture-perfect people, scales, and so on-I do not want this to be some generic, cookie-cutter weight loss web site. This is about weight loss from a different point of view-and I don't think this will come across in the webpage, but the concept will be introduced later. It's about weight loss as a byproduct of changing eating habits from unhealthy to healthy.

```html
<!DOCTYPE html>
<html lang="en">
<head>
<meta charset="utf-8">
<title>brightpathYOU – Healthy Eating, Lasting Weight Loss</title>
<link rel="stylesheet" href="https://fonts.googleapis.com/css2?family=Kreon:wght@400;500&family=Open+Sans:ital,wght@0,400;0,600;0,700;1,400&display=swap">
<style>
:root{
  --nav-top:#1d66a6;
  --nav-bottom:#0d4273;
  --nav-active:#0a355e;
  --brand-blue:#0f4f8c;
  --link-blue:#1a63a8;
  --text:#5a5a5a;
  --text-dark:#333;
  --rule:#dcdcdc;
  --panel:#f4f4f4;
  --sidebar-bg:#f5f5f5;
  --footer-light:#f3f3f3;
  --footer-dark:#222;
  --footer-darker:#171717;
  --white:#fff;
}
*{box-sizing:border-box;margin:0;padding:0}
html,body{width:1200px;height:2436px;overflow:hidden;background:var(--white)}
body{font-family:"Open Sans",Arial,sans-serif;color:var(--text);position:relative}
.abs{position:absolute}

/* header */
.site-header{left:0;top:0;width:1200px;height:76px;background:linear-gradient(var(--nav-top),var(--nav-bottom))}
.brand{left:100px;top:12px;font-family:"Kreon",Georgia,serif;font-size:40px;color:var(--white);letter-spacing:.5px;line-height:48px}
.main-nav{right:99px;top:0;display:flex;height:76px}
.main-nav a{display:block;color:#cfe0f1;font-size:14px;line-height:76px;padding:0 16px;text-decoration:none;text-transform:uppercase}
.main-nav a.is-active{background:var(--nav-active);color:var(--white)}

/* hero */
.hero{left:0;top:76px;width:1200px;height:475px;background:
 radial-gradient(ellipse 500px 200px at 200px 420px,rgba(196,140,80,.65),transparent 70%),
 radial-gradient(ellipse 400px 380px at 960px 300px,rgba(40,100,170,.55),transparent 70%),
 linear-gradient(180deg,#111a26 0%,#223247 45%,#4c4a4a 80%,#141414 100%)}
.hero-caption{left:100px;font-size:31px;color:var(--white);background:rgba(25,25,25,.78);padding:0 14px;line-height:44px}
.hero-dots{left:551px;top:519px;width:99px;height:22px;border-radius:11px;background:rgba(0,0,0,.55);display:flex;justify-content:center;align-items:center;gap:8px}
.hero-dots span{width:10px;height:10px;border-radius:50%;background:#ddd}
.hero-dots span.is-on{background:transparent;border:2px solid #ddd}

/* promo */
.promo-video{left:100px;top:568px;width:493px;height:158px;background:linear-gradient(90deg,#8b5a2b,#c48a4a 40%,#b9b9b9 50%,#c48a4a 60%,#7e4f25)}
.play{position:absolute;left:50%;top:50%;transform:translate(-50%,-50%)}
.optin{left:609px;top:568px;width:492px;height:158px;background:linear-gradient(#f8f8f8,#e6e6e6);border:1px solid #d2d2d2}
.optin-title{position:absolute;left:14px;top:12px;width:470px;font-size:17px;font-weight:600;line-height:23px;color:var(--brand-blue)}
.optin-title .lead{font-size:14.5px}
.optin-fields{position:absolute;left:12px;top:74px;display:flex;gap:3px}
.optin-fields span{display:block;width:154px;height:29px;background:var(--white);border:1px solid #d4d4d4;font-size:12px;color:#999;line-height:27px;padding-left:12px}
.optin-offer{position:absolute;left:12px;top:110px;font-size:29px;color:#c3c3c3;line-height:40px}
.btn-subscribe{position:absolute;right:10px;top:114px;width:84px;height:32px;border-radius:3px;background:linear-gradient(#4f95dc,#2a6fb7);color:var(--white);font-size:13px;font-weight:600;text-align:center;line-height:32px}

/* posts */
.post{left:100px;width:741px}
.post-title{border-left:6px solid var(--brand-blue);padding-left:16px;height:69px}
.post-title h2{font-size:19.5px;font-weight:600;color:var(--brand-blue);line-height:28px;padding-top:4px}
.post-meta{display:flex;align-items:center;font-size:13px;color:#666;margin-top:2px;gap:6px}
.post-meta .sep{margin:0 6px}
.share{display:flex;align-items:center;gap:4px;margin-left:8px}
.share .btn{height:19px;border:1px solid #c8d3e1;background:#eef2f8;font-size:11px;font-weight:600;color:#3b5b8f;padding:0 5px 0 4px;display:flex;align-items:center;gap:3px;border-radius:2px}
.share .btn i{display:block;width:11px;height:11px;background:currentColor;border-radius:2px}
.share .btn.red{background:#e25a3a;border-color:#d04a2a;color:var(--white)}
.share .btn.plus{background:#fff;border-color:#ddd;color:#d44}
.share .count{height:19px;border:1px solid #ccc;font-size:10.5px;padding:0 5px;line-height:17px;color:#555;border-radius:2px;margin-right:6px}
.post-body{display:flex;margin-top:14px;gap:15px}
.post-thumb{position:relative;width:374px;height:218px;flex:none}
.post-text{font-size:13.5px;line-height:21.5px;color:#555}
.post-text p{margin-bottom:8px}
.more{font-size:12.5px;font-weight:600;color:var(--brand-blue);text-transform:uppercase;margin-top:14px}
.post-rule{position:absolute;left:0;bottom:0;width:741px;height:1px;background:var(--rule)}

.pager{left:568px;top:1882px;display:flex;align-items:center;gap:9px}
.pager span{display:block;width:30px;height:29px;border-radius:3px;background:#e9e9e9;color:#888;font-size:13px;text-align:center;line-height:29px}
.pager .nav{background:#555;color:#fff}
.pager .is-current{background:var(--link-blue);color:var(--white)}
.pager .gap{background:none;width:auto;letter-spacing:2px}

/* sidebar */
.archives{left:859px;top:773px;width:242px;height:531px;background:var(--sidebar-bg)}
.archives h3{height:39px;background:linear-gradient(var(--nav-top),var(--nav-bottom));color:var(--white);font-size:18px;font-weight:600;line-height:39px;padding-left:17px}
.archives ul{list-style:none;padding:17px 0 0 20px}
.archives li{font-size:14.5px;color:#8a8a8a;line-height:35.5px}
.archives li::before{content:"•";margin-right:9px;color:#aaa}
.side-ad{left:891px;top:1315px;width:171px;height:626px;background:linear-gradient(180deg,#fff 0%,#fff 8%,#f7b34a 18%,#fff 32%,#f3efe8 60%,#f39a2a 82%,#fff 88%,#8fc53a 94%,#fff 100%)}

/* footer */
.footer-top{left:0;top:1981px;width:1200px;height:252px;background:var(--footer-light)}
.f-col{top:2010px;width:250px}
.f-col h4{font-size:16.5px;font-weight:400;color:#444;margin-bottom:18px}
.f-col p{font-size:12px;line-height:20.5px;color:#888}
.f-col strong{display:block;color:#555;font-size:13px;margin-bottom:2px}
.f-col .know{font-size:12.5px;color:var(--link-blue);margin-top:6px}
.f-divider{top:2007px;width:1px;height:210px;background:#d6d6d6}
.f-input{width:206px;height:30px;border:1px solid #ccc;background:var(--white);font-size:11px;color:#444;line-height:28px;padding-left:10px;margin-bottom:10px}
.btn-submit{margin-left:136px;width:70px;height:28px;background:linear-gradient(#777,#4a4a4a);color:var(--white);font-size:13px;font-weight:700;text-align:center;line-height:28px;border-radius:2px}
.connect{list-style:none}
.connect li{display:flex;align-items:center;font-size:12px;color:#888;height:29px;margin-bottom:12.5px}
.connect li i{width:28px;height:28px;border-radius:3px;background:var(--c);margin-right:10px;flex:none}
.connect li b{font-weight:400;color:var(--link-blue);font-size:14px;margin-left:4px}
.connect li.red b{color:#b71c1c}
.footer-bottom{left:0;top:2233px;width:1200px;height:203px;background:var(--footer-dark)}
.f-links{top:2255px;left:0;width:1200px;text-align:center;font-size:12.5px;color:#ccc}
.f-links span{margin:0 9px;color:#888}
.copyright{top:2290px;left:0;width:1200px;text-align:center;font-size:12.5px;color:#ccc}
.disclaimer{left:100px;top:2330px;width:1001px;height:86px;background:var(--footer-darker);border-radius:3px;padding:12px 18px;font-size:11.5px;line-height:20px;font-style:italic;color:#6c6c6c;text-align:center}
</style>
</head>
<body>

<header class="site-header abs">
  <div class="brand abs">brightpath you</div>
  <nav class="main-nav abs">
    <a class="is-active">Home</a><a>About me</a><a>Blog</a><a>Recipes</a><a>Products</a><a>Contact us</a>
  </nav>
</header>

<section class="hero abs" role="img" aria-label="Slideshow photo: runner silhouetted on a hill at sunset, with a smiling man in a blue sweater on the right">
</section>
<div class="hero-caption abs" style="top:257px">no hunger, no deprivation, no pills,</div>
<div class="hero-caption abs" style="top:310px">no weighing foods or calorie counting</div>
<div class="hero-dots abs"><span class="is-on"></span><span></span><span></span><span></span></div>

<div class="promo-video abs" role="img" aria-label="Video thumbnail: bare feet on a bathroom scale on a wooden floor">
  <svg class="play" width="84" height="84" viewBox="0 0 84 84"><circle cx="42" cy="42" r="38" fill="rgba(0,0,0,.35)" stroke="#fff" stroke-width="5"/><path d="M33 26 L60 42 L33 58 Z" fill="#fff"/></svg>
</div>
<div class="optin abs">
  <div class="optin-title"><span class="lead">Every Plate Tells A Story, Every Meal Builds A Habit-</span><br>-And How You Can Shape Yours Today</div>
  <div class="optin-fields"><span>First name</span><span>Last name</span><span>E-mail</span></div>
  <div class="optin-offer">Free video &amp; eBook</div>
  <div class="btn-subscribe">Subscribe</div>
</div>

<!-- posts -->
<article class="post abs" style="top:778px;height:323px">
  <div class="post-title"><h2>Phasellus tellus ligula, fermentum ut consequat sed, accumsan ut magna</h2>
    <div class="post-meta">April 7, 2014 <span>&nbsp;at&nbsp; 10.15 A.M</span><span class="sep">/</span>Post by : Ned Brook<span class="sep">/</span>
      <div class="share"><span class="btn"><i></i>Like</span><span class="count">3k</span><span class="btn"><i></i>Post</span><span class="count">316</span><span class="btn plus">+1</span><span class="count">81</span><span class="btn red"><i></i>Share</span><span class="count">4.6K</span></div>
    </div>
  </div>
  <div class="post-body">
    <div class="post-thumb" role="img" aria-label="Video thumbnail: two people training with dumbbells in a gym" style="background:linear-gradient(90deg,#3a3a3a,#9a8f86 45%,#7aa6c4 75%,#2f3b46)">
      <svg class="play" width="50" height="36" viewBox="0 0 50 36"><rect width="50" height="36" rx="6" fill="rgba(0,0,0,.75)"/><path d="M19 9 L34 18 L19 27 Z" fill="#fff"/></svg>
    </div>
    <div class="post-text">
      <p>Maecenas consequat semper dolor eu posuere. Phasellus tincidunt sapien metus, nec accumsan erat pharetra id. Donec iaculis ipsum vel nisl congue, nec lacinia turpis volutpat. Vivamus sit amet molestie risus. Nam erat sem, pharetra consectetur scelerisque sed, auctor in ligula. Sed massa nunc, volutpat vel lorem ut.</p>
      <p>Sed pellentesque nulla dapibus, laoreet nibh at, commodo erat. Nullam posuere, ipsum blandit aliquam fringilla, nulla lectus venenatis enim.</p>
      <div class="more">More</div>
    </div>
  </div>
  <div class="post-rule"></div>
</article>

<article class="post abs" style="top:1155px;height:323px">
  <div class="post-title"><h2>Phasellus tellus ligula, fermentum ut consequat sed, accumsan ut magna</h2>
    <div class="post-meta">April 7, 2014 <span>&nbsp;at&nbsp; 10.15 A.M</span><span class="sep">/</span>Post by : Ned Brook<span class="sep">/</span>
      <div class="share"><span class="btn"><i></i>Like</span><span class="count">3k</span><span class="btn"><i></i>Post</span><span class="count">316</span><span class="btn plus">+1</span><span class="count">81</span><span class="btn red"><i></i>Share</span><span class="count">4.6K</span></div>
    </div>
  </div>
  <div class="post-body">
    <div class="post-thumb" role="img" aria-label="Video thumbnail: woman lifting a red dumbbell" style="background:linear-gradient(90deg,#6e6e6e,#b5b5b5 45%,#8c6a55 70%,#3e3e3e)">
      <svg class="play" width="50" height="36" viewBox="0 0 50 36"><rect width="50" height="36" rx="6" fill="rgba(0,0,0,.75)"/><path d="M19 9 L34 18 L19 27 Z" fill="#fff"/></svg>
    </div>
    <div class="post-text">
      <p>Maecenas consequat semper dolor eu posuere. Phasellus tincidunt sapien metus, nec accumsan erat pharetra id. Donec iaculis ipsum vel nisl congue, nec lacinia turpis volutpat. Vivamus sit amet molestie risus. Nam erat sem, pharetra consectetur scelerisque sed, auctor in ligula. Sed massa nunc, volutpat vel lorem ut.</p>
      <p>Sed pellentesque nulla dapibus, laoreet nibh at, commodo erat. Nullam posuere, ipsum blandit aliquam fringilla, nulla lectus venenatis enim.</p>
      <div class="more">More</div>
    </div>
  </div>
  <div class="post-rule"></div>
</article>

<article class="post abs" style="top:1532px;height:323px">
  <div class="post-title"><h2>Phasellus tellus ligula, fermentum ut consequat sed, accumsan ut magna</h2>
    <div class="post-meta">April 7, 2014 <span>&nbsp;at&nbsp; 10.15 A.M</span><span class="sep">/</span>Post by : Ned Brook<span class="sep">/</span>
      <div class="share"><span class="btn"><i></i>Like</span><span class="count">3k</span><span class="btn"><i></i>Post</span><span class="count">316</span><span class="btn plus">+1</span><span class="count">81</span><span class="btn red"><i></i>Share</span><span class="count">4.6K</span></div>
    </div>
  </div>
  <div class="post-body">
    <div class="post-thumb" role="img" aria-label="Video thumbnail: woman drinking water beside a bowl of salad at a kitchen table" style="background:linear-gradient(90deg,#9c9c9c,#d8d4cc 40%,#c9b9a6 60%,#4a4a4a)">
      <svg class="play" width="50" height="36" viewBox="0 0 50 36"><rect width="50" height="36" rx="6" fill="rgba(0,0,0,.75)"/><path d="M19 9 L34 18 L19 27 Z" fill="#fff"/></svg>
    </div>
    <div class="post-text">
      <p>Maecenas consequat semper dolor eu posuere. Phasellus tincidunt sapien metus, nec accumsan erat pharetra id. Donec iaculis ipsum vel nisl congue, nec lacinia turpis volutpat. Vivamus sit amet molestie risus. Nam erat sem, pharetra consectetur scelerisque sed, auctor in ligula. Sed massa nunc, volutpat vel lorem ut.</p>
      <p>Sed pellentesque nulla dapibus, laoreet nibh at, commodo erat. Nullam posuere, ipsum blandit aliquam fringilla, nulla lectus venenatis enim.</p>
      <div class="more">More</div>
    </div>
  </div>
  <div class="post-rule"></div>
</article>

<div class="pager abs"><span class="nav">»</span><span class="is-current">1</span><span>2</span><span>3</span><span>4</span><span class="gap">....</span><span>20</span></div>

<!-- sidebar -->
<aside class="archives abs">
  <h3>Archives</h3>
  <ul>
    <li>Integer lobortis</li><li>Curabitur ac</li><li>Phasellus tellus nisl</li><li>Aenean fringilla</li><li>Vestibulum</li><li>Aliquam commodo</li><li>Integer lobortis</li><li>Curabitur ac</li><li>Phasellus tellus nisl</li><li>Aenean fringilla</li><li>Vestibulum</li><li>Aliquam commodo</li><li>Integer lobortis</li>
  </ul>
</aside>
<div class="side-ad abs" role="img" aria-label="NovaHost banner advertisement: 25% off hosting plans, with a woman holding a glass and a green 'see more' button"></div>

<!-- footer -->
<footer>
  <div class="footer-top abs"></div>
  <div class="f-col abs" style="left:100px;width:230px">
    <h4>About Me</h4>
    <p>Cras faucibus sapien at arcu dignissim interdum. Sed tempus leo nulla, eget auctor tortor pharetra a. Morbi et gravida tortor, vitae cursus odio amet felis eleifend molestie morbi tristique senectus et netus et malesuada</p>
    <div class="know">Know more</div>
  </div>
  <div class="f-divider abs" style="left:346px"></div>
  <div class="f-col abs" style="left:372px;width:230px">
    <h4>Latest Blog</h4>
    <p><strong>Morbi sit amet consequat diam</strong>Cras faucibus sapien at arcu dignissim interdum. Sed tempus leo nulla, eget auctor tortor pharetra a. Morbi et gravida tortor, vitae cursus odio amet felis eleifend molestie</p>
    <div class="know">Know more</div>
  </div>
  <div class="f-divider abs" style="left:622px"></div>
  <div class="f-col abs" style="left:648px">
    <h4>Email Signup</h4>
    <div class="f-input">Name</div>
    <div class="f-input">Email ID</div>
    <div class="btn-submit">SUBMIT</div>
  </div>
  <div class="f-divider abs" style="left:882px"></div>
  <div class="f-col abs" style="left:908px">
    <h4>Connect with us</h4>
    <ul class="connect">
      <li style="--c:#3b5b98"><i></i>Join with us on <b>FriendSquare</b></li>
      <li style="--c:#3ba9e0"><i></i>Follow us on <b>Chirpline</b></li>
      <li style="--c:#1f6c9e"><i></i>Share on <b>WorkLink</b></li>
      <li class="red" style="--c:#c4302b"><i></i>Watch on <b>ViewStream</b></li>
    </ul>
  </div>

  <div class="footer-bottom abs"></div>
  <div class="f-links abs">Home<span>|</span>About me<span>|</span>Blog<span>|</span>Recipes<span>|</span>Products<span>|</span>Contact us</div>
  <div class="copyright abs">Copyright &copy; 2014 &nbsp; Ned Brook &nbsp; All rights reserved.</div>
  <div class="disclaimer abs">This website expresses the opinions of the author, is intended for informational and educational purposes only, should not be construed as medical or dietary advice, and is not intended to be a substitute for same. Before changing diets, medications, or before undertaking a weight loss regimen, be sure to consult with your physician. This information is not intended to diagnose or treat any illness or health problems you may be experiencing, so kindly address your doctor with these concerns</div>
</footer>

</body>
</html>
```